packaging design for cosmetics line

It's called Corvessa cosmetics. The line consists middle end face body and hair products. I think a colorful artwork will be good to make the product more appealing . The packaging color should be either black or white,
Face:
Undereye cream gel , Gel contour des yeux (15mL tube)
Anti acne night treatment, Traitement anti acné (30mL tube)
Day moisturizer SPF 20, Hydratant quotidien SPF 20 (50 mL bottle pump)
Green clay face mask , Masque à l'argile verte (200mL tube)
Toner for dry to normal Skins, Tonique pour les peaux normales à séches
(200mL bottle)
Gentle make up remover , Démaquillant doux (200 mL TUBE)

Hair:
Gentle hair shampoo , sulfates free , Shampoing doux sans sulfates(350mL bottle ,flip top cap)
Nourishing hair conditioner , Après shampoing nourissant(350mL bottle , flip top cap)
Light formulat hair moisturizer, Hydratant cheveux formule légère ( 200mL pump bottle)

Body:

Skin repair body cream, Crème réparatrice pour le corps (200mL jar)
Waterproof sunblock SPF 50, Protection solaire résistante à l'eau (250mL tube)
20% Glycolic acid peel (200 mL pump Bottle )
Daily body moisturizer , Hydratant quotidien pour le corps (350 ml bottle)
(350 mL pump bottle)

Some packaging that inspire me:
Contestants can make a design for one item in each category and do the remaining when they are selected.
http://www.quillbatch.co.nz/blog/2010/04/frostpine-takes-silver-for-package-design
http://www.boxmarrow.com/blog/?a_aid=7142cdde¤tPage=575
http://www.pixelharbourfiles.com/2013/07/35-beautiful-cosmetic-packaging-designs.html
http://www.wrapgrove.com/applications/personal-care/skincare-products-get-green-packaging
http://lumbrix.co.nz/our-work/sensitive-skincare-packaging/

Reason: No one submitted design I fancy

I need stickers designs , not the containers

Target Market(s)

Middle end beauty products for women

Industry/Entity Type

Hair

Requirements
Must have
• french and english product description. French in bigger script
Nice to have
• Colorful artwork , not too heavy though, please see pictures attached

```html
<!DOCTYPE html>
<html lang="en">
<head>
<meta charset="utf-8">
<title>Corvessa Cosmetics – Label Designs</title>
<link href="https://fonts.googleapis.com/css2?family=Open+Sans:wght@400;600&family=Parisienne&display=swap" rel="stylesheet">
<style>
  :root {
    --canvas: #f3f1f0;
    --label: #ffffff;
    --label-edge: #e6e3e1;
    --brand-grey: #8d8d8d;
    --rule: #b9b9b9;
    --text-grey: #7a7a7a;
    --text-strong: #6a6a6a;
    --script-red: #e0404a;
    --petal-deep: #e23a44;
    --petal-mid: #ef7a84;
    --petal-light: #fbd9dc;
    --stem: #3c8a3a;
  }
  * { margin: 0; padding: 0; box-sizing: border-box; }
  html, body {
    width: 1031px;
    height: 1200px;
    overflow: hidden;
    background: var(--canvas);
  }
  .canvas {
    position: relative;
    width: 1031px;
    height: 1200px;
  }
  .label {
    position: absolute;
    background: var(--label);
    border: 1px solid var(--label-edge);
    border-radius: 6px;
    display: flex;
    flex-direction: column;
    align-items: center;
    font-family: "Open Sans", sans-serif;
  }
  .label--tube { left: 160px; top: 360px; width: 300px; height: 620px; }
  .label--bottle { left: 570px; top: 250px; width: 300px; height: 830px; }

  .brand {
    margin-top: 72px;
    display: flex;
    flex-direction: column;
    align-items: center;
    gap: 10px;
  }
  .brand__rule { width: 96px; height: 1px; background: var(--rule); }
  .brand__name {
    font-family: "Open Sans", sans-serif;
    font-weight: 400;
    font-size: 22px;
    letter-spacing: 4px;
    text-transform: uppercase;
    color: var(--brand-grey);
    text-align: center;
    line-height: 1.25;
  }
  .label--bottle .brand__name { font-size: 24px; }

  .artwork {
    align-self: flex-start;
    margin-left: 26px;
    width: 236px;
    height: 300px;
    border-radius: 48% 52% 46% 54% / 44% 40% 60% 56%;
    background:
      radial-gradient(circle at 42% 34%, var(--petal-light) 0 14%, transparent 34%),
      radial-gradient(circle at 50% 38%, var(--petal-mid) 0 36%, transparent 60%),
      linear-gradient(170deg, var(--petal-deep) 0%, var(--petal-mid) 55%, rgba(60,138,58,0.55) 100%);
    opacity: 0.85;
  }
  .label--tube .artwork { margin-top: 30px; height: 290px; }
  .label--bottle .artwork { margin-top: 70px; height: 340px; width: 250px; }

  .name-fr {
    font-family: "Parisienne", cursive;
    color: var(--script-red);
    font-size: 27px;
    line-height: 1.05;
    text-align: center;
    margin-top: 22px;
  }
  .label--bottle .name-fr { margin-top: 40px; }
  .name-rule { width: 170px; height: 1px; background: var(--rule); margin-top: 8px; }
  .name-en {
    margin-top: 8px;
    font-size: 12px;
    letter-spacing: 1.4px;
    color: var(--text-grey);
    text-transform: uppercase;
    text-align: center;
    line-height: 1.45;
  }
  .name-en strong { font-weight: 600; color: var(--text-strong); }
  .volume {
    margin-top: 26px;
    font-size: 12px;
    letter-spacing: 1px;
    color: var(--text-grey);
  }
  .label--bottle .volume { margin-top: 52px; }
</style>
</head>
<body>
<main class="canvas">

  <section class="label label--tube" aria-label="Gentle make up remover label">
    <div class="brand">
      <span class="brand__rule"></span>
      <span class="brand__name">Corvessa<br>Cosmetics</span>
      <span class="brand__rule"></span>
    </div>
    <div class="artwork" role="img" aria-label="Watercolour illustration of a red carnation with a green stem"></div>
    <p class="name-fr">Démaquillant doux</p>
    <span class="name-rule"></span>
    <p class="name-en">Gentle <strong>Make up<br>remover</strong></p>
    <p class="volume">200 mL</p>
  </section>

  <section class="label label--bottle" aria-label="Daily body moisturizer label">
    <div class="brand">
      <span class="brand__rule"></span>
      <span class="brand__name">Corvessa<br>Cosmetics</span>
      <span class="brand__rule"></span>
    </div>
    <div class="artwork" role="img" aria-label="Watercolour illustration of a red carnation with a green stem"></div>
    <p class="name-fr">Hydratant quotidien<br>pour le corps</p>
    <span class="name-rule"></span>
    <p class="name-en">Daily body <strong>moisturizer</strong></p>
    <p class="volume">350 mL</p>
  </section>

</main>
</body>
</html>
```